Modern brochure by Lawyers, for modern clients

It'sa "News" for their clients. Attached you can find the current News without design. It must be elegant but very attractive and modern. Their web site is http://www.montalbanyasociados.cl/ Their expertise is labor and employment practice area. It must be in editable format so that lawyers can write the news in a template with this corporate design.

Target Market(s)

Big Companies

Font styles to use
Sans Serif

Colors
0255a3
474747

Requirements
Nice to have
• Legal Pictures and only a little of yellow. One touch! It must be in editable format so that lawyers can write the news in a template with this corporate design.

```html
<!DOCTYPE html>
<html lang="es">
<head>
<meta charset="utf-8">
<title>Boletín laboral – Montalbán y Asociados</title>
<link href="https://fonts.googleapis.com/css2?family=Merriweather:wght@300;400;700&display=swap" rel="stylesheet">
<style>
  :root {
    --ink-navy: #34506c;
    --ink-body: #2e2e2e;
    --slate: #7f97a6;
    --steel: #3f6a8f;
    --mist: #b9cdd6;
    --pale: #dbe7ea;
    --backdrop: #eceae6;
    --paper: #ffffff;
  }
  html, body {
    margin: 0;
    width: 1200px;
    height: 1100px;
    overflow: hidden;
    background: var(--backdrop);
    font-family: "Merriweather", Georgia, serif;
  }
  .page {
    position: absolute;
    left: 256px;
    top: 48px;
    width: 704px;
    height: 1000px;
    background: var(--paper);
    overflow: hidden;
    box-shadow: 0 2px 6px rgba(0,0,0,.12);
  }
  .brand {
    position: absolute;
    left: 42px;
    top: 60px;
    display: flex;
    align-items: center;
    gap: 6px;
    color: var(--ink-navy);
  }
  .brand-dot {
    width: 22px; height: 22px;
    border-radius: 50%;
    background: var(--ink-navy);
  }
  .brand-name {
    font-weight: 300;
    font-size: 14px;
    line-height: 15px;
    letter-spacing: .5px;
    border-right: 2px solid var(--ink-navy);
    padding-right: 5px;
  }
  .brand-name small { display: block; font-size: 10px; color: var(--ink-navy); }
  .date {
    position: absolute;
    right: 62px;
    top: 58px;
    font-size: 14px;
    font-weight: 300;
    color: var(--ink-navy);
  }
  .deco-circle {
    position: absolute;
    left: -54px;
    top: 599px;
    width: 296px; height: 296px;
    border-radius: 50%;
    background: var(--pale);
  }
  .photo-column {
    position: absolute;
    left: 0; top: 193px;
    width: 213px;
  }
  .photo-column div { height: 120px; }
  .photo-columns { background: linear-gradient(90deg, #dfe9ec, #c4d4da 60%, #e4ecee); }
  .photo-glasses { background: linear-gradient(160deg, #d9d6d2, #b9b3ad 60%, #cfc9c2); }
  .tile-slate { background: var(--slate); }
  .photo-crowd { background: linear-gradient(180deg, #4a7094, #3d6388); }
  .letter {
    position: absolute;
    left: 262px;
    top: 190px;
    width: 379px;
    color: var(--ink-body);
  }
  .letter h1 {
    margin: 0 0 36px;
    font-weight: 400;
    font-size: 24px;
    color: var(--ink-navy);
  }
  .letter p {
    margin: 0 0 19px;
    font-size: 10.5px;
    font-weight: 300;
    line-height: 19px;
    text-align: justify;
  }
  .letter .cta {
    margin-top: 30px;
    font-size: 12.5px;
    line-height: 19px;
    font-weight: 400;
    color: var(--ink-navy);
    text-align: left;
  }
  .cta a { color: var(--slate); font-weight: 700; text-decoration: none; }
  .closing {
    position: absolute;
    left: 230px;
    top: 773px;
    font-size: 10.5px;
    font-weight: 300;
    color: var(--ink-body);
  }
  .signature {
    position: absolute;
    left: 220px;
    width: 250px;
    top: 804px;
    text-align: center;
    font-size: 10.5px;
    font-weight: 700;
    line-height: 19px;
    color: var(--ink-navy);
  }
  .footer-bars {
    position: absolute;
    left: 0; top: 980px;
    width: 704px; height: 7px;
    display: flex;
  }
  .footer-bars span:nth-child(1) { width: 179px; background: var(--ink-navy); }
  .footer-bars span:nth-child(2) { width: 170px; background: var(--slate); }
  .footer-bars span:nth-child(3) { width: 176px; background: var(--mist); }
  .footer-bars span:nth-child(4) { flex: 1; background: var(--pale); }
</style>
</head>
<body>
<main class="page">
  <header>
    <div class="brand">
      <span class="brand-dot"></span>
      <span class="brand-name">MONTALBÁN<small>ASOCIADOS ABOGADOS</small></span>
    </div>
    <div class="date">Santiago, 25 de julio de 2018</div>
  </header>

  <div class="deco-circle"></div>

  <aside class="photo-column">
    <div class="photo-columns" role="img" aria-label="Fotografía de columnas clásicas de un edificio judicial"></div>
    <div class="photo-glasses" role="img" aria-label="Fotografía de unos lentes sobre un computador portátil"></div>
    <div class="tile-slate"></div>
    <div class="photo-crowd" role="img" aria-label="Fotografía aérea de personas caminando"></div>
  </aside>

  <article class="letter">
    <h1>Estimados,</h1>
    <p>Por medio del presente, les damos a conocer el Dictamen Ordinario N° 3826-031, emitido por la Dirección del Trabajo el pasado 20 de julio, relativo a los “beneficios históricos”.</p>
    <p>Estos fueron definidos en su oportunidad por este organismo como “…aquellos beneficios que se han otorgado desde siempre…” por parte del empleador.</p>
    <p>A partir de este Dictamen, el cual reconsidera el criterio del anterior Director del Trabajo, los beneficios históricos vuelven a ser patrimonio de la empresa y de los trabajadores que los han recibido, dejando de serlo de la organización sindical y de sus socios beneficiados por el solo hecho de haberse “replicado” en un instrumento colectivo durante una negociación.</p>
    <p>Por último, el Dictamen en comento aclara que si un “beneficio histórico” se incrementa de manera real y efectiva producto de una negociación colectiva, únicamente dicho incremento se entenderá originado en el respectivo instrumento colectivo, y en consecuencia, objeto de una posible extensión en el evento de que ésta se haya acordado durante la negociación.</p>
    <p class="cta">Para mayor análisis de lo resuelto por la Dirección del Trabajo, se puede revisar el Dictámen en comento <a href="http://www.montalbanyasociados.cl/">haciendo click aquí</a></p>
  </article>

  <p class="closing">Sin otro particular, saluda atentamente a ustedes,</p>
  <div class="signature">
    Montalbán y Asociados Abogados<br>
    oficina@montalbanyasociados.cl
  </div>

  <div class="footer-bars"><span></span><span></span><span></span><span></span></div>
</main>
</body>
</html>
```